Brim Physiotherapy Business Card

I need a business card to allow for promotion of my new business as well as to book patients in for appointments.
The business is a pelvic floor health physiotherapy practice specialising in women's and men's continence type care.
It will be a small business offering personal care.
I will be the sole practitioner to start off with.

Target Market(s)

Pregnant and post natal women
Aging women and men
Women with breastfeeding difficulties
Children with bedwetting issues

Industry/Entity Type

Business

Contact Information for Business Card

Previous designs have perhaps been a bit too basic or not really eye catching.

Colors

Designer to choose colors to be used in the design.

Requirements
Must have
• Option to write appointment time and date on the back.
• Attractive and eye catching front.
• Logo somewhere on the card.
Nice to have
• Bright colours.
• Simple design that is easy to print.

```html
<!DOCTYPE html>
<html lang="en">
<head>
<meta charset="utf-8">
<title>Brim Physiotherapy Business Card</title>
<link rel="stylesheet" href="https://fonts.googleapis.com/css2?family=Montserrat:wght@400;500;600;700&display=swap">
<style>
  :root {
    --canvas: #e4e4e4;
    --card: #ffffff;
    --lilac: #c9a0cc;
    --lilac-text: #c393c6;
    --charcoal: #4a4a4c;
    --slate: #6d6e71;
    --ink: #3c3c3e;
    --white: #ffffff;
  }
  * { box-sizing: border-box; margin: 0; padding: 0; }
  html, body { width: 1200px; height: 1000px; overflow: hidden; }
  body {
    background: var(--canvas);
    font-family: "Montserrat", sans-serif;
    position: relative;
  }
  .card {
    position: absolute;
    left: 291px;
    width: 618px;
    height: 352px;
    background: var(--card);
    overflow: hidden;
  }
  .card-front { top: 96px; }
  .card-back { top: 500px; height: 353px; }
  .panel { position: absolute; left: 0; top: 0; width: 618px; height: 312px; }
  .footer-band {
    position: absolute; left: 0; right: 0; bottom: 0; height: 40px;
    background: var(--charcoal); color: var(--white);
    display: flex; align-items: center; justify-content: center;
  }
  .tagline { font-size: 20px; font-weight: 500; letter-spacing: 0.3px; }
  .notice { font-size: 14.5px; letter-spacing: 2.2px; }

  /* front */
  .brand { position: absolute; left: 22px; top: 54px; width: 220px; text-align: center; }
  .brand-dot { width: 100px; height: 100px; border-radius: 50%; background: var(--slate); margin: 0 auto 12px; }
  .brand-name { font-size: 30px; font-weight: 700; line-height: 1.1; color: var(--slate); }
  .practitioner { position: absolute; right: 17px; top: 100px; font-size: 21px; font-weight: 500; color: var(--ink); }
  .practitioner .surname { color: var(--white); font-weight: 600; }
  .credentials { position: absolute; right: 17px; top: 180px; list-style: none; text-align: right; color: var(--ink); font-size: 16px; line-height: 21px; }
  .credentials li { position: relative; padding-right: 15px; margin-bottom: 10px; }
  .credentials li::after {
    content: ""; position: absolute; right: 0; top: 7px; width: 8px; height: 8px; border-radius: 50%; background: var(--ink);
  }

  /* back */
  .field-label { position: absolute; left: 23px; top: 34px; font-size: 13px; color: var(--lilac-text); }
  .rule { position: absolute; height: 2px; background: var(--lilac); }
  .rule-name { left: 23px; top: 52px; width: 450px; }
  .appt-heading { position: absolute; left: 124px; top: 66px; font-size: 18px; font-weight: 700; color: var(--lilac-text); }
  .days { position: absolute; left: 23px; top: 112px; display: flex; gap: 0; }
  .day { display: flex; align-items: center; font-size: 17px; font-weight: 700; color: var(--lilac-text); margin-right: 24px; }
  .day .box { width: 26px; height: 26px; border: 2px solid var(--lilac); margin-right: 6px; }
  .day:nth-child(4) { margin-right: 16px; }
  .rule-date { left: 23px; top: 200px; width: 203px; }
  .at { position: absolute; left: 234px; top: 188px; font-size: 15px; color: var(--lilac-text); }
  .rule-time { left: 262px; top: 200px; width: 154px; }
  .meridiem { position: absolute; left: 426px; top: 166px; font-size: 15px; line-height: 21px; color: var(--lilac-text); }
  .contacts { position: absolute; left: 23px; top: 218px; list-style: none; }
  .contacts li { display: flex; align-items: center; height: 31px; font-size: 18.5px; color: var(--ink); }
  .contacts li.phone { font-weight: 600; }
  .contacts svg { width: 27px; height: 27px; margin-right: 12px; }
</style>
</head>
<body>

<section class="card card-front">
  <svg class="panel" viewBox="0 0 618 312" role="img" aria-label="Lilac panel where the brand figure decoration sits">
    <path d="M300 0 C268 70 248 150 252 215 C256 265 290 295 318 312 L618 312 L618 0 Z" fill="var(--lilac)"/>
  </svg>

  <div class="brand">
    <div class="brand-dot"></div>
    <p class="brand-name">Brim<br>Physiotherapy</p>
  </div>

  <h1 class="practitioner">Maya<span class="surname">Hollis</span></h1>

  <ul class="credentials">
    <li>B Physiotherapy</li>
    <li>PGradCert PelvicFloor<br>Physiotherapy (Hons)</li>
    <li>Cert III in Fitness</li>
  </ul>

  <div class="footer-band"><p class="tagline">women's health and pelvic foor physiotherapy</p></div>
</section>

<section class="card card-back">
  <svg class="panel" viewBox="0 0 618 312" role="img" aria-label="Lilac panel where the brand figure decoration sits">
    <path d="M522 0 C500 80 470 170 478 245 C484 285 505 302 522 312 L618 312 L618 0 Z" fill="var(--lilac)"/>
  </svg>

  <span class="field-label">name:</span>
  <div class="rule rule-name"></div>

  <h2 class="appt-heading">Your next appointment is</h2>

  <div class="days">
    <span class="day"><span class="box"></span>MON</span>
    <span class="day"><span class="box"></span>TUE</span>
    <span class="day"><span class="box"></span>WED</span>
    <span class="day"><span class="box"></span>THURS</span>
    <span class="day"><span class="box"></span>FRI</span>
  </div>

  <div class="rule rule-date"></div>
  <span class="at">AT</span>
  <div class="rule rule-time"></div>
  <span class="meridiem">A.M<br>P.M</span>

  <ul class="contacts">
    <li>
      <svg viewBox="0 0 28 28" aria-hidden="true">
        <circle cx="14" cy="14" r="14" fill="var(--lilac)"/>
        <g fill="none" stroke="var(--white)" stroke-width="1.4">
          <circle cx="14" cy="14" r="7"/>
          <ellipse cx="14" cy="14" rx="3" ry="7"/>
          <line x1="7" y1="14" x2="21" y2="14"/>
        </g>
      </svg>www.brimphysio.com.au
    </li>
    <li class="phone">
      <svg viewBox="0 0 28 28" aria-hidden="true">
        <circle cx="14" cy="14" r="14" fill="var(--lilac)"/>
        <path d="M10 7 L12.5 7 L13.5 10.5 L11.8 11.8 C12.8 14 14 15.2 16.2 16.2 L17.5 14.5 L21 15.5 L21 18 C21 19.5 19.5 20.5 18 20.2 C12.5 19 9 15.5 7.8 10 C7.5 8.5 8.5 7 10 7 Z" fill="var(--white)"/>
      </svg>0412583047
    </li>
    <li>
      <svg viewBox="0 0 28 28" aria-hidden="true">
        <circle cx="14" cy="14" r="14" fill="var(--lilac)"/>
        <rect x="7" y="9" width="14" height="10" fill="var(--white)"/>
        <path d="M7 9 L14 15 L21 9" fill="none" stroke="var(--lilac)" stroke-width="1.4"/>
      </svg>maya@brimphysio.com.au
    </li>
  </ul>

  <div class="footer-band"><p class="notice">If unable to keep appointment, kindly give 24 hours notice.</p></div>
</section>

</body>
</html>
```